New business logo / Business Card Design

My company provides Interim Management and consultancy, for Facilities Services. Covers any aspect of facilities management, including M&E, helpdesk, asset management, supplier relationships, catering, cleaning etc. Company provides innovative solutions to exceed client needs, drawing on years of experience. Initial thoughts on logo are attached below. Fits with RAG status on projects, red, amber and green, with logo design colours around moving services from amber to green.

Target Market(s)

Facilities Management clients and service providers

Industry/Entity Type

Business

Contact Information for Business Card

Company Name = k7Rventures Ltd My name on card = Derek Haskins, Director Mobile = 07912365048 Email = Derek@k7rventuresltd.co.uk Twitter = @k7Rventures Ltd

Font styles to use
Sans Serif

Colors
f37122
00a990

Requirements
Must have
• Logo to be evident, with some background image in reference to Facilities Management

```html
<!DOCTYPE html>
<html lang="en">
<head>
<meta charset="utf-8">
<title>k7Rventures Ltd – Business Card</title>
<link rel="stylesheet" href="https://fonts.googleapis.com/css2?family=Roboto:wght@400;500;700;900&display=swap">
<style>
  :root {
    --backdrop: #e8e5e1;
    --card-white: #ffffff;
    --brand-orange: #f26a21;
    --panel-black: #000000;
    --ink: #111111;
    --on-dark: #ffffff;
  }
  * { margin: 0; padding: 0; box-sizing: border-box; }
  html, body {
    width: 1200px;
    height: 902px;
    overflow: hidden;
    background: var(--backdrop);
    font-family: "Roboto", Arial, sans-serif;
  }
  .business-card {
    position: absolute;
    left: 100px;
    top: 121px;
    width: 1000px;
    height: 659px;
    background: var(--card-white);
    overflow: hidden;
    box-shadow: 0 10px 30px rgba(0,0,0,0.18);
  }
  .card-swoosh {
    position: absolute;
    inset: 0;
    width: 100%;
    height: 100%;
  }
  .swoosh-orange { fill: var(--brand-orange); }
  .swoosh-black { fill: var(--panel-black); }
  .company-name {
    position: absolute;
    left: 79px;
    top: 130px;
    font-size: 52px;
    font-weight: 900;
    color: var(--ink);
    letter-spacing: 0.5px;
    line-height: 1;
  }
  .holder {
    position: absolute;
    right: 50px;
    top: 392px;
    text-align: right;
    color: var(--on-dark);
    line-height: 1;
  }
  .holder-name {
    font-size: 35px;
    font-weight: 500;
    letter-spacing: 0.3px;
  }
  .holder-title {
    font-size: 27px;
    font-weight: 400;
    margin-top: 2px;
  }
  .contact-list {
    position: absolute;
    right: 50px;
    top: 500px;
    list-style: none;
    color: var(--on-dark);
  }
  .contact-row {
    display: flex;
    justify-content: flex-end;
    align-items: center;
    gap: 12px;
    height: 32px;
    margin-bottom: 5.5px;
    font-size: 29px;
    font-weight: 400;
    line-height: 1;
  }
  .contact-icon {
    width: 31px;
    height: 31px;
    flex: none;
    display: block;
  }
  .icon-bg { fill: var(--brand-orange); }
  .icon-line { fill: none; stroke: var(--panel-black); stroke-width: 2; }
</style>
</head>
<body>
  <main class="business-card">
    <svg class="card-swoosh" viewBox="0 0 815 537" preserveAspectRatio="none" aria-hidden="true">
      <path class="swoosh-orange" d="M664,0 L815,0 L815,537 L134,537 C420,445 625,270 664,0 Z"/>
      <path class="swoosh-black" d="M815,20 C730,230 500,440 134,537 L815,537 Z"/>
    </svg>

    <h1 class="company-name">k7Rventures Ltd</h1>

    <div class="holder">
      <p class="holder-name">Derek Haskins</p>
      <p class="holder-title">Director</p>
    </div>

    <ul class="contact-list">
      <li class="contact-row">
        <span class="contact-text">07912365048</span>
        <svg class="contact-icon" viewBox="0 0 31 31" aria-label="Mobile">
          <rect class="icon-bg" width="31" height="31"/>
          <rect class="icon-line" x="10" y="5" width="11" height="21" rx="1.5"/>
          <line class="icon-line" x1="12" y1="21" x2="19" y2="21"/>
        </svg>
      </li>
      <li class="contact-row">
        <span class="contact-text">Derek@k7rventuresltd.co.uk</span>
        <svg class="contact-icon" viewBox="0 0 31 31" aria-label="Email">
          <rect class="icon-bg" width="31" height="31"/>
          <rect class="icon-line" x="5" y="8" width="21" height="15"/>
          <polyline class="icon-line" points="5,8 15.5,17 26,8"/>
        </svg>
      </li>
      <li class="contact-row">
        <span class="contact-text">@k7Rventures Ltd</span>
        <svg class="contact-icon" viewBox="0 0 31 31" aria-label="Social handle">
          <rect class="icon-bg" width="31" height="31"/>
        </svg>
      </li>
    </ul>
  </main>
</body>
</html>
```